Democracy in crisis book

This book tries to sound the ALARM that we will lose our democracy unless we force Unionists to adopt the plan inside this book. I designed a mock cover (attached) but I am concerned it would not look good in the Thumbnail view that most people would see it as they're scrolling down Shopvale or Pagenook. The final title for the book is: Final Hour to Rescue the Free Republic. The current subtitle is: The Single Path to Halt the 2022 Partisan Takeover & Renew Our Homeland -- but it’s a work in progress.The subtitle is still working progress but it's really not that important and can be small.
STYLE CONSIDERATIONS:
(1) The title should be on 5 separate lines: Final; Hour; To Rescue; Free; Republic
(2) The title could be in white fat letters except for maybe one line that says “To Rescue” which could be in the blue color of the Civic Union Party-- or maybe Free Republic could be in blue. We may have to try a few variations of that.
(3) I picked the red in the mock cover to connotate an emergency,
(4) I liked big bold fat font going across the full page so that it looks like a major warning sign, though note I was unable to extend each line flush all the way to the right which I think would have been better.
(5) I liked it better flush to left instead of centered.
(6) I picked the Harwick monument + a crowd for my mock cover, but a picture of a huge crowd protesting with a picture of the United States Congress in the background would be much better. DO NOT USE HARWICK. Obviously I would need it to be an open license or something I can pay a small amount to get. If you can find that picture then the page should probably be colored in red with Congress in white.
I got the idea 4 giant title from the book “seldom a quiet so bright” and Dellowby’s “When Freedom Fades” or “Grey Herons” by Mara Vostell though I hate that font)
I love Osric Thale’s “marked since the outset” cover so if you find a picture of Congress and a protest crowd instead of painting it red you could have just a couple of jagged red stripes going across it like that cover.
I love the 3-D effect of Greta Wolven's cover for The Silverwren where it looks like a page is being ripped. That effect could be done the words Free Republic like it's being torn off the page UPDATE: MANY DESIGNERS TRIED THAT & IT DID NOT WORK AT ALL.
Note that this book will be submitted to many award competitions, so please give me an award-winning cover.
I like how the title of the book The Unchosen by Martin Fellowes has the words starting to fade. I don't like the ladder on it, but maybe 'Free Republic' could fade like that.
Unionists

```html
<!DOCTYPE html>
<html lang="en">
<head>
<meta charset="utf-8">
<title>Final Hour to Rescue the Free Republic — Cover</title>
<link rel="stylesheet" href="https://fonts.googleapis.com/css2?family=Anton&family=Roboto+Condensed:wght@400;700&display=swap">
<style>
  :root {
    --stage: #2b2b2b;
    --cover-black: #111111;
    --cover-charcoal: #1d1d1d;
    --alarm-red: #8e1a1f;
    --union-blue: #3f7fcf;
    --title-white: #eeeeee;
    --stone-light: #e6e4e0;
    --stone-mid: #a9a6a1;
    --stone-dark: #5a5854;
  }
  * { margin: 0; padding: 0; box-sizing: border-box; }
  html, body { width: 1200px; height: 800px; overflow: hidden; }
  body {
    background: var(--stage);
    display: flex;
    align-items: center;
    justify-content: center;
  }
  .book-cover {
    position: relative;
    width: 500px;
    height: 750px;
    overflow: hidden;
    background: radial-gradient(ellipse at 40% 35%, var(--cover-charcoal), var(--cover-black) 75%);
    box-shadow: 0 10px 30px rgba(0,0,0,0.5);
  }
  .capitol-photo {
    position: absolute;
    left: 120px;
    top: 250px;
    width: 300px;
    height: 340px;
    border-radius: 150px 150px 0 0;
    background: linear-gradient(180deg, var(--stone-light) 0%, var(--stone-mid) 60%, var(--stone-dark) 100%);
    opacity: 0.85;
  }
  .crowd-photo {
    position: absolute;
    left: 0;
    bottom: 0;
    width: 500px;
    height: 280px;
    background: linear-gradient(160deg, rgba(230,228,224,0) 0%, var(--stone-mid) 30%, var(--stone-light) 60%, #f2f1ee 100%);
  }
  .author-name {
    position: absolute;
    top: 26px;
    left: 0;
    width: 100%;
    text-align: center;
    font-family: 'Roboto Condensed', sans-serif;
    font-weight: 400;
    font-size: 22px;
    letter-spacing: 9px;
    color: var(--title-white);
    text-transform: uppercase;
  }
  .title-block {
    position: absolute;
    left: 0;
    top: 60px;
    width: 500px;
    height: 520px;
  }
  .title-block text {
    font-family: 'Anton', 'Oswald', sans-serif;
    text-transform: uppercase;
  }
  .title-final, .title-hour { fill: var(--alarm-red); }
  .title-rescue { fill: var(--union-blue); }
  .title-free { fill: var(--title-white); }
  .subtitle {
    position: absolute;
    left: 26px;
    bottom: 46px;
    width: 440px;
    font-family: 'Roboto Condensed', sans-serif;
    font-weight: 700;
    font-size: 21px;
    line-height: 1.2;
    color: var(--alarm-red);
  }
</style>
</head>
<body>
  <main class="book-cover">
    <div class="capitol-photo" role="img" aria-label="Photograph of the Congress building dome"></div>
    <div class="crowd-photo" role="img" aria-label="Photograph of a protesting crowd with raised arms"></div>

    <p class="author-name">Corwin Ashby Delmont</p>

    <svg class="title-block" viewBox="0 0 500 520" aria-label="Final Hour to Rescue the Free Republic">
      <defs>
        <linearGradient id="republic-fade" x1="0" y1="0" x2="0" y2="1">
          <stop offset="0" stop-color="#eeeeee" stop-opacity="0.95"/>
          <stop offset="1" stop-color="#eeeeee" stop-opacity="0.1"/>
        </linearGradient>
      </defs>
      <text class="title-final" x="22" y="170" font-size="190" textLength="456" lengthAdjust="spacingAndGlyphs">Final</text>
      <text class="title-hour" x="22" y="290" font-size="128" textLength="456" lengthAdjust="spacingAndGlyphs">Hour</text>
      <text class="title-rescue" x="22" y="350" font-size="58" textLength="456" lengthAdjust="spacingAndGlyphs">To Rescue</text>
      <text class="title-free" x="22" y="440" font-size="96" textLength="456" lengthAdjust="spacingAndGlyphs">Free</text>
      <text x="22" y="515" font-size="80" fill="url(#republic-fade)" textLength="456" lengthAdjust="spacingAndGlyphs">Republic</text>
    </svg>

    <p class="subtitle">The Single Path to Halt the 2022 Partisan Takeover &amp; Renew Our Homeland</p>
  </main>
</body>
</html>
```